Producer Needs a Movie Poster for a Dramatic Film

We need a movie poster for a new dramatic film called "Past the Lantern".
Synopisis: A young drug addict (cocaine and alcohol), ROSS PENDRY, has hit rock bottom after a continuous downward spiral of alcoholism and drug abuse, leaving him with nothing to live for. His ex-girlfriend left him. His best friend doesn’t want anything to do with him. Unable to rehabilitate himself after multiple attempts, he attempts suicide (Jumping off of a high-rise apartment building).
We want the poster to give the dark feel of the film. It should be serious and personable.
We want the three lead actors to be listed on the top of the poster from left to right (Gregory Lint, Miriam Kessub, Osric Demmelby).
The title of the film, Past the Lantern, should be in the center of the poster.
We want "Coming Soon" centered on the bottom of the poster.

No pictures will be provided for this poster, so be creative and make something special for us to use. We're looking for a variety of good ideas.

We're excited to see what you come up with!

Please, make sure you provide us with files we can easily use. Also, we would like a copy of the film title in a separate file for easy use as well. So, two files total (One with the poster, One with just the film title by itself).

Industry/Entity Type

Movie

Requirements
Must have
• We want the three lead actors to be listed on the top of the poster from left to right (Gregory Lint, Miriam Kessub, Osric Demmelby).
• The title of the film, Past the Lantern, should be in the center of the poster.
• We want "Coming Soon" centered on the bottom of the poster.
• Please, make sure you provide us with files we can easily use. Also, we would like a copy of the film title in a separate file for easy use as well. So, two files total (One with the poster, One with just the film title by itself).
Should not have
• Should not have a person on the poster unless they are unrecognizable and you can't see any characteristics. We can't have someone on the poster who won't be in the movie.
• Don't put each locations that won't be in the film either. It takes place in LOs Angeles. Mostly on a high-rise apartment building rooftop.

```html
<!DOCTYPE html>
<html lang="en">
<head>
<meta charset="utf-8">
<title>Past the Lantern — Poster</title>
<link rel="stylesheet" href="https://fonts.googleapis.com/css2?family=Cinzel:wght@400&display=swap">
<style>
  :root {
    --ink-dark: #121416;
    --ink-mid: #262c30;
    --ground: #9a9284;
    --ground-light: #b8afa0;
    --tile-teal: #24545a;
    --tile-ochre: #a58a2e;
    --tile-rust: #9a3e2a;
    --crane-red: #b0505a;
    --denim: #4a79a8;
    --denim-deep: #284a78;
    --text-light: #f2f0ec;
  }
  html, body {
    margin: 0;
    padding: 0;
    width: 873px;
    height: 1200px;
    overflow: hidden;
    background: var(--ink-dark);
  }
  .poster {
    position: relative;
    width: 873px;
    height: 1200px;
    overflow: hidden;
    font-family: "Cinzel", "Times New Roman", serif;
    color: var(--text-light);
  }
  .poster__scene {
    position: absolute;
    inset: 0;
    background:
      radial-gradient(ellipse 22% 32% at 22% 92%, rgba(74,121,168,0.95), transparent 75%),
      radial-gradient(ellipse 16% 22% at 58% 88%, rgba(74,121,168,0.85), transparent 75%),
      radial-gradient(ellipse 14% 16% at 32% 62%, rgba(40,74,120,0.9), transparent 75%),
      radial-gradient(ellipse 20% 38% at 63% 38%, rgba(184,175,160,0.85), transparent 72%),
      radial-gradient(ellipse 10% 24% at 52% 22%, rgba(176,80,90,0.7), transparent 75%),
      radial-gradient(ellipse 18% 30% at 90% 25%, rgba(165,138,46,0.55), transparent 75%),
      radial-gradient(ellipse 22% 26% at 82% 90%, rgba(154,62,42,0.65), transparent 75%),
      radial-gradient(ellipse 22% 20% at 30% 20%, rgba(165,138,46,0.5), transparent 75%),
      radial-gradient(ellipse 20% 22% at 15% 60%, rgba(154,62,42,0.4), transparent 75%),
      linear-gradient(100deg, var(--tile-teal) 0%, var(--ink-mid) 30%, var(--ground) 55%, var(--ink-mid) 78%, var(--tile-teal) 100%);
  }
  .poster__shade {
    position: absolute;
    inset: 0;
    background:
      radial-gradient(ellipse 70% 65% at 55% 55%, transparent 35%, rgba(10,12,14,0.75) 100%),
      linear-gradient(180deg, rgba(10,12,14,0.6) 0%, transparent 18%, transparent 85%, rgba(10,12,14,0.4) 100%);
  }
  .cast {
    position: absolute;
    top: 37px;
    left: 0;
    width: 100%;
    height: 34px;
    margin: 0;
    padding: 0;
    list-style: none;
  }
  .cast__name {
    position: absolute;
    top: 0;
    transform: translateX(-50%);
    white-space: nowrap;
    font-size: 24px;
    text-transform: uppercase;
  }
  .cast__name--first { left: 184px; }
  .cast__name--second { left: 442px; }
  .cast__name--third { left: 697px; }
  .title {
    position: absolute;
    inset: 0;
    margin: 0;
    font-weight: 400;
    font-size: 94px;
    line-height: 1;
  }
  .title__line {
    position: absolute;
    white-space: nowrap;
  }
  .title__line--one { left: 195px; top: 371px; }
  .title__line--two { left: 268px; top: 484px; }
  .title__line--three { left: 320px; top: 587px; }
  .release {
    position: absolute;
    left: 0;
    width: 100%;
    top: 1096px;
    text-align: center;
    font-size: 24px;
    text-transform: uppercase;
    margin: 0;
  }
</style>
</head>
<body>
  <main class="poster">
    <div class="poster__scene" role="img" aria-label="Point-of-view photo looking straight down from a high-rise rooftop edge: legs in jeans and blue sneakers dangling over colorful tiled tower facades and a construction site far below"></div>
    <div class="poster__shade"></div>
    <ul class="cast">
      <li class="cast__name cast__name--first">Gregory Lint</li>
      <li class="cast__name cast__name--second">Miriam Kessub</li>
      <li class="cast__name cast__name--third">Osric Demmelby</li>
    </ul>
    <h1 class="title">
      <span class="title__line title__line--one">PAST</span>
      <span class="title__line title__line--two">THE</span>
      <span class="title__line title__line--three">LANTERN</span>
    </h1>
    <p class="release">Coming Soon</p>
  </main>
</body>
</html>
```